Event Website for the Audio & Visual Industry

Convene is an exhibition aimed at meeting the business needs of audio and visual professionals – the visitors are the ones that make purchase decisions when buying anything to do with AV installation, Lighting & Entertainment Technology, DJ Technologies and even Musical Instruments.

We need to rebuild our website to reflect the professional look but with a bit of creativity/flare that is associated with the industry.

Websites whose design is along the lines we're looking for:

• http:www.marlowtech.com.au
• http:www.quenra.com
• http://www.brightpanelfair.example/ (competitor expo, like the layout. Not fantastic though, but the best I’ve seen from the industry)
• http://www.velmora.com.au and http://www.tralvick.com.au/ (Like these brand websites, they are clean and corporate but the use of imagery allows it to have some personality)

Target Market(s)

Corporate AV End Users, Lighting Designers, Concert/Entertainment companies, Sound Engineers

Industry/Entity Type

Business

Requirements
Must have
• Refer to the current splash page – www.convene-expo.example
This is the look and feel we have developed for our brochure. We want to expand on this and create a professional corporate look and feel without alienating existing sound, light and vision sectors.

The website's focus is to register visitors to attend the show. Please include a floating 'Register Free' Call to action. Please also include floating social media buttons. For what I mean by 'floating' check out the Social media buttons on this website: http://feedlorn.example/2012/02/19/glass-tower-trailer/ (scroll down to see effect).

We'll like to include a Rotating Banner at the top.

Sponsor element at the bottom off the page.

Sign up form functionality

Menu to be: About the Show, What's On, Register, How to Exhibit, Blog, Contact us.

I would like to see designs for a content page as well as the homepage.

```html
<!DOCTYPE html>
<html lang="en">
<head>
<meta charset="utf-8">
<title>Convene 2012 – Sound, Light, Vision</title>
<link rel="stylesheet" href="https://fonts.googleapis.com/css2?family=Barlow:wght@400;500;600;700&display=swap">
<style>
:root{
  --red:#c8102e;
  --ink:#1c1c1c;
  --nav:#1e1e1e;
  --grey:#9a9a9a;
  --text:#2b2b2b;
  --page:#e8e9ea;
  --tab:#e6e6e6;
  --line:#d4d4d4;
  --accent-line:#2a9fc2;
}
*{box-sizing:border-box;margin:0;padding:0}
html,body{width:1200px;height:1148px;overflow:hidden}
body{background:var(--page);font-family:'Barlow',sans-serif;color:var(--text);position:relative}
.stage-band{position:absolute;left:0;top:279px;width:1200px;height:313px;background:linear-gradient(#3c3c3c,#1c1c1c);border-top:2px solid var(--accent-line)}
.page{position:absolute;left:147px;top:11px;width:909px;height:1137px;background:#fff;box-shadow:0 0 18px rgba(0,0,0,.25)}
.header{position:absolute;left:147px;top:11px;width:909px;height:198px}
.brand{position:absolute;left:36px;top:66px;display:flex;align-items:center;gap:10px}
.brand-mark{width:14px;height:14px;border-radius:50%;background:var(--red)}
.brand-name{font-size:52px;font-weight:500;color:var(--ink);letter-spacing:-1px}
.register-btn{position:absolute;right:0;top:0;width:174px;height:53px;background:var(--red);color:#fff;font-weight:600;font-size:19px;display:flex;align-items:center;justify-content:center;letter-spacing:.5px}
.event-date{position:absolute;right:36px;top:86px;text-align:right}
.event-date .dates{color:var(--red);font-size:34px;font-weight:500;line-height:1}
.event-date .venue{font-size:14.5px;font-weight:700;color:#333;margin-top:9px;letter-spacing:.3px}
.event-date .locale{font-size:14.5px;font-weight:600;color:#b0b0b0;letter-spacing:.3px}
.main-nav{position:absolute;left:147px;top:209px;width:909px;height:55px;background:var(--nav);display:flex}
.main-nav a{color:#fff;text-decoration:none;font-size:12px;font-weight:700;letter-spacing:2.3px;display:flex;align-items:center;justify-content:center;border-right:1px solid #3c3c3c;height:100%}
.main-nav a:last-child{border-right:0}
.hero{position:absolute;left:138px;top:269px;width:927px;height:312px;display:flex}
.hero-slide{position:relative;width:744px;height:312px;background:linear-gradient(135deg,#4a3660 0%,#6b4fa0 40%,#3a2c55 70%,#1d1a26 100%)}
.hero-caption{position:absolute;left:0;top:211px;width:531px;height:84px;background:rgba(0,0,0,.68);padding:13px 12px 0 36px;color:#fff;font-size:23px;line-height:28px;letter-spacing:-.3px}
.hero-caption .line{display:block;white-space:nowrap}
.hero-caption a{color:var(--red);font-size:20px;text-decoration:none}
.hero-tabs{width:183px;display:flex;flex-direction:column}
.hero-tab{height:78px;background:var(--tab);border-bottom:1px solid #d2d2d2;display:flex;align-items:center;padding-left:23px;font-size:13.5px;font-weight:600;color:#222}
.hero-tab.active{background:#f1f1f1;border-left:6px solid var(--red);color:var(--red);padding-left:17px}
.float-cta{position:absolute;left:0;top:297px;width:81px}
.float-cta .badge{height:68px;background:#fff;display:flex;align-items:center;justify-content:center;font-size:15px;font-weight:500;color:var(--ink)}
.float-cta .cta{height:48px;background:var(--red);color:#fff;font-size:13.5px;font-weight:700;line-height:14px;padding:10px 10px}
.features{position:absolute;left:159px;top:618px;display:flex;gap:7px}
.feature{position:relative;height:165px}
.feature .photo{height:129px}
.feature .label{height:36px;background:#111;color:#fff;font-size:14.5px;font-weight:600;display:flex;align-items:center;padding-left:12px;letter-spacing:.3px;white-space:nowrap}
.info{position:absolute;left:147px;top:814px;width:909px;height:100px}
.col h2{color:var(--red);font-size:18px;font-weight:600;letter-spacing:.3px;margin-bottom:8px}
.col p{font-size:13.5px;line-height:16px;color:#222}
.exhibitors{position:absolute;left:24px;top:0;width:262px}
.exhibitors .more{display:block;color:var(--red);font-size:12.5px;margin-top:8px;text-decoration:none}
.divider{position:absolute;top:0;width:1px;height:95px;background:var(--line)}
.newsletter{position:absolute;left:320px;top:0;width:270px}
.signup{display:flex;gap:7px;margin-top:12px}
.signup input{width:195px;height:30px;border:1px solid #ccc;border-radius:3px;padding-left:10px;font-family:inherit;font-size:11px;color:#aaa}
.signup button{width:65px;height:30px;border:1px solid #ccc;border-radius:3px;background:linear-gradient(#fff,#e9e9e9);font-family:inherit;font-weight:600;font-size:13px}
.actions{position:absolute;left:618px;top:0;width:262px;display:flex;flex-direction:column;gap:15px}
.action{height:40px;border:1px solid #ccc;border-radius:2px;background:linear-gradient(#fff,#eee);display:flex;align-items:center;gap:14px;padding-left:20px;font-size:13px;font-weight:600;letter-spacing:1.2px;color:#222;white-space:nowrap}
.sponsors{position:absolute;left:147px;top:940px;width:909px;height:109px;background:var(--nav)}
.sponsors .title{position:absolute;left:34px;top:43px;color:#777;font-size:16.5px;font-weight:600}
.sponsor{position:absolute;top:40px;color:#fff;font-size:24px;font-weight:600;transform:translateX(-50%);white-space:nowrap}
.legal{position:absolute;left:164px;top:1066px;font-size:10px;line-height:15px;color:#333}
.credit{position:absolute;left:885px;top:1068px;font-size:10px;color:#222}
.credit .name{font-size:26px;font-weight:700;color:#aaa;margin-top:4px}
</style>
</head>
<body>
<div class="stage-band"></div>
<div class="page"></div>

<header class="header">
  <div class="brand"><span class="brand-name">convene</span><span class="brand-mark"></span></div>
  <a class="register-btn">REGISTER FREE</a>
  <div class="event-date">
    <div class="dates">21st-23rd AUGUST 2012</div>
    <div class="venue">HARBOURSIDE CONVENTION &amp; EXHIBITION CENTRE</div>
    <div class="locale">HARBOURSIDE PRECINCT, AUSTRALIA</div>
  </div>
</header>

<nav class="main-nav">
  <a style="width:196px">ABOUT THE SHOW</a>
  <a style="width:139px">WHAT'S ON</a>
  <a style="width:136px">REGISTER</a>
  <a style="width:180px">HOW TO EXHIBIT</a>
  <a style="width:103px">BLOG</a>
  <a style="width:155px">CONTACT US</a>
</nav>

<section class="hero">
  <div class="hero-slide" role="img" aria-label="Sound engineer working at a large mixing console on the show floor under purple lighting">
    <div class="hero-caption">
      <span class="line">Discover some of the latest technology from</span>
      <span class="line">some of the industry leaders. <a>Learn More</a></span>
    </div>
  </div>
  <div class="hero-tabs">
    <div class="hero-tab active">DISCOVER THE LATEST</div>
    <div class="hero-tab">FEATURED KEYNOTE</div>
    <div class="hero-tab">NEW PRODUCTS</div>
    <div class="hero-tab">NEW LOCATION</div>
  </div>
</section>

<aside class="float-cta">
  <div class="badge">convene</div>
  <div class="cta">REGISTER<br>FOR FREE</div>
</aside>

<section class="features">
  <div class="feature" style="width:287px">
    <div class="photo" role="img" aria-label="Studio monitors and a digital mixing desk on display" style="background:linear-gradient(135deg,#2b3a5c,#6a7fb0 50%,#1c2233)"></div>
    <div class="label">DISCOVER THE LATEST ADVANCEMENTS</div>
  </div>
  <div class="feature" style="width:292px">
    <div class="photo" role="img" aria-label="Exhibitor stand with an angled video wall" style="background:linear-gradient(135deg,#222,#5a6a80 50%,#111)"></div>
    <div class="label">TALK TO INDUSTRY PROFESSIONALS</div>
  </div>
  <div class="feature" style="width:293px">
    <div class="photo" role="img" aria-label="Seated audience at an industry keynote session" style="background:linear-gradient(135deg,#3a3030,#7a6a66 50%,#2a2424)"></div>
    <div class="label">ATTEND INDUSTRY &nbsp;KEYNOTES</div>
  </div>
</section>

<section class="info">
  <div class="col exhibitors">
    <h2>FEATURED EXHIBITORS</h2>
    <p>Velmora, Tralvick, Quenra, Harwin &amp; Gale, Ostra, BoardMark, Pellan, FormHaus, Klangwerk, Audiolume, Jorvik, Kessan</p>
    <a class="more">AND MANY MORE...</a>
  </div>
  <div class="divider" style="left:300px"></div>
  <div class="col newsletter">
    <h2>CONVENE NEWSLETTER</h2>
    <p style="font-size:12.5px;line-height:16px">Sign up for the newsletter and get year-round information source on Convene.</p>
    <form class="signup"><input type="text" value="enter your email" aria-label="Email address"><button type="button">submit</button></form>
  </div>
  <div class="divider" style="left:602px"></div>
  <div class="actions">
    <div class="action">
      <svg width="18" height="22" viewBox="0 0 18 22" aria-hidden="true"><path d="M0 0h13l5 5v17H0z" fill="#c8102e"/><path d="M4 15c3-1 6-6 5-9-1 3 1 7 5 8" stroke="#fff" stroke-width="1.4" fill="none"/></svg>
      DOWNLOAD THE FLOORPLAN
    </div>
    <div class="action" style="letter-spacing:.6px">
      <svg width="30" height="18" viewBox="0 0 30 18" aria-hidden="true"><g fill="#777"><circle cx="8" cy="5" r="3.5"/><circle cx="22" cy="5" r="3.5"/><circle cx="15" cy="6" r="4"/><path d="M1 18c0-5 3-7 7-7s7 2 7 7z"/><path d="M15 18c0-5 3-7 7-7s7 2 7 7z"/><path d="M7 18c0-5 3-7 8-7s8 2 8 7z" fill="#555"/></g></svg>
      CONTACT THE CONVENE TEAM
    </div>
  </div>
</section>

<section class="sponsors">
  <div class="title">OUR SPONSORS</div>
  <div class="sponsor" style="left:323px">avlink global</div>
  <div class="sponsor" style="left:537px">meridale</div>
  <div class="sponsor" style="left:756px">convene</div>
</section>

<footer>
  <div class="legal">
    STRICTLY TRADE ONLY. Entry is restricted to members of the ICT, Audio Visual and Entertainment industries.<br>
    Persons not in these categories, including children will not be admitted at any time.<br>
    © 2012 Meridale Exhibitions, Australia. All rights reserved. Level 3, 118 Harlow Street, Sydney, NSW 2000, Australia.<br>
    Telephone: +61 2 9555 0140. Facsimile: +61 2 9555 0141.
  </div>
  <div class="credit">Brought to you by<div class="name">meridale</div></div>
</footer>
</body>
</html>
```